Bright Meadow Counseling Business Card design with a visually interesting use of Space

I need business cards that are luxurious and give a peaceful, calm vibe. I also had some letterhead designed, and i like the look of it also, it's attached with the logo design for reference/ ideas but feel free to be creative.

Target Market(s)

High end luxurious client who needs counseling

Industry/Entity Type

Marriage and Family Therapy

Contact Information for Business Card

Mira Kowalczyk MS LMFT/ or Toby Hallett address 4150 Larkin Suite 600

Font styles to use
Sans Serif

Colors
0054AA
0677BA
7BADD7
CADEEF
E8F1F8
0094D4
00A9DD
6FCCEA
C7EBF8
E9F6FB
A7469A
B969AE
D3A5CF
EDDBEB
F8F0F9
6B429C
8869AF
B7A5CE
E3DAEB
F3F0F8

Requirements
Must have
• Logo and color scheme but be simple modern and luxurious
Nice to have
• I'd like to incorporate some elelmets from the logo and letterhead into a simple modern card

```html
<!DOCTYPE html>
<html lang="en">
<head>
<meta charset="UTF-8">
<title>Bright Meadow Counseling — Business Card</title>
<link href="https://fonts.googleapis.com/css2?family=Montserrat:wght@200;300;400;600;700&display=swap" rel="stylesheet">
<style>
  :root {
    --stage: #3f3f3f;
    --paper: #ffffff;
    --ink: #1d1d1d;
    --ink-soft: #555555;
    --night: #111111;
    --night-edge: #1c1c1c;
    --plum: #6b429c;
    --orchid: #8b2a94;
    --sky: #22a5dc;
    --lagoon: #36b3bb;
    --accent: #a7469a;
  }
  * { box-sizing: border-box; margin: 0; padding: 0; }
  html, body {
    width: 1200px; height: 1200px; overflow: hidden;
    background: var(--stage);
    font-family: "Montserrat", sans-serif;
  }
  .card {
    position: absolute; left: 180px;
    width: 840px; height: 480px;
    border-radius: 34px; overflow: hidden;
  }
  .card--front { top: 60px; background: var(--paper); }
  .card--back {
    top: 620px;
    background: linear-gradient(115deg, var(--night) 0%, var(--night-edge) 55%, var(--night) 100%);
  }

  .wordmark { position: absolute; display: flex; flex-direction: column; align-items: flex-end; }
  .wordmark__row { display: flex; align-items: center; gap: 14px; }
  .wordmark__dot { border-radius: 50%; background: var(--accent); }
  .wordmark__name { font-weight: 200; line-height: 1; letter-spacing: 0.01em; }
  .wordmark__sub { font-weight: 200; letter-spacing: 0.32em; line-height: 1; }

  .card--front .wordmark { left: 0; right: 0; top: 80px; align-items: center; }
  .card--front .wordmark__inner { display: flex; flex-direction: column; align-items: flex-end; }
  .card--front .wordmark__dot { width: 22px; height: 22px; }
  .card--front .wordmark__name { font-size: 58px; color: var(--ink); }
  .card--front .wordmark__sub { font-size: 22px; color: var(--ink); margin-top: 6px; margin-right: -6px; }

  .identity {
    position: absolute; left: 70px; top: 300px;
    padding-left: 20px; border-left: 6px solid var(--orchid);
  }
  .identity__name { font-weight: 700; font-size: 30px; color: var(--orchid); text-transform: uppercase; letter-spacing: 0.01em; line-height: 1.05; }
  .identity__title { font-weight: 400; font-size: 22px; color: var(--ink-soft); line-height: 1.15; }

  .divider { position: absolute; left: 440px; top: 245px; width: 1.5px; height: 130px; background: var(--orchid); }

  .contact { position: absolute; left: 480px; top: 248px; list-style: none; }
  .contact__item { display: flex; align-items: flex-start; gap: 12px; font-size: 16px; font-weight: 400; color: var(--ink); line-height: 1.25; margin-bottom: 9px; }
  .contact__icon { width: 18px; height: 18px; flex: none; margin-top: 1px; fill: var(--orchid); }

  .stripe { position: absolute; left: 0; right: 0; bottom: 0; height: 24px; display: flex; }
  .stripe__seg--plum { flex: 20; background: var(--plum); }
  .stripe__seg--orchid { flex: 32; background: var(--orchid); }
  .stripe__seg--sky { flex: 32; background: var(--sky); }
  .stripe__seg--lagoon { flex: 16; background: var(--lagoon); }

  .card--back .wordmark { left: 0; right: 0; top: 175px; align-items: center; }
  .card--back .wordmark__inner { display: flex; flex-direction: column; align-items: flex-end; }
  .card--back .wordmark__dot { width: 28px; height: 28px; }
  .card--back .wordmark__name { font-size: 72px; color: #ffffff; }
  .card--back .wordmark__sub { font-size: 27px; color: #ffffff; margin-top: 8px; margin-right: -8px; }
</style>
</head>
<body>

<section class="card card--front">
  <div class="wordmark">
    <div class="wordmark__inner">
      <div class="wordmark__row">
        <span class="wordmark__dot"></span>
        <span class="wordmark__name">Bright Meadow</span>
      </div>
      <span class="wordmark__sub">Counseling</span>
    </div>
  </div>

  <div class="identity">
    <p class="identity__name">Mira Kowalczyk</p>
    <p class="identity__title">MS LMFT</p>
  </div>

  <div class="divider"></div>

  <ul class="contact">
    <li class="contact__item">
      <svg class="contact__icon" viewBox="0 0 24 24"><path d="M6.6 10.8a15.1 15.1 0 0 0 6.6 6.6l2.2-2.2a1 1 0 0 1 1-.25 11.4 11.4 0 0 0 3.6.57 1 1 0 0 1 1 1V20a1 1 0 0 1-1 1A17 17 0 0 1 3 4a1 1 0 0 1 1-1h3.5a1 1 0 0 1 1 1c0 1.25.2 2.45.57 3.6a1 1 0 0 1-.25 1z"/></svg>
      <span>555-214-7730</span>
    </li>
    <li class="contact__item">
      <svg class="contact__icon" viewBox="0 0 24 24"><path d="M7 3h10v5H7z"/><path d="M4 9h16a1 1 0 0 1 1 1v7h-4v4H7v-4H3v-7a1 1 0 0 1 1-1zm5 7v3h6v-3z"/></svg>
      <span>555-214-7731</span>
    </li>
    <li class="contact__item">
      <svg class="contact__icon" viewBox="0 0 24 24"><path d="M3 5h18v14H3z" fill="none"/><path d="M3 5h18l-9 7zM3 7.2l9 7 9-7V19H3z"/></svg>
      <span>hello@brightmeadowcare.com</span>
    </li>
    <li class="contact__item">
      <svg class="contact__icon" viewBox="0 0 24 24"><path d="M12 2a7 7 0 0 0-7 7c0 5.2 7 13 7 13s7-7.8 7-13a7 7 0 0 0-7-7zm0 9.5A2.5 2.5 0 1 1 12 6.5a2.5 2.5 0 0 1 0 5z"/></svg>
      <span>4150 Larkin Suite 600<br>Fairview, Oregon 97024</span>
    </li>
  </ul>

  <div class="stripe">
    <span class="stripe__seg--plum"></span>
    <span class="stripe__seg--orchid"></span>
    <span class="stripe__seg--sky"></span>
    <span class="stripe__seg--lagoon"></span>
  </div>
</section>

<section class="card card--back">
  <div class="wordmark">
    <div class="wordmark__inner">
      <div class="wordmark__row">
        <span class="wordmark__dot"></span>
        <span class="wordmark__name">Bright Meadow</span>
      </div>
      <span class="wordmark__sub">Counseling</span>
    </div>
  </div>
</section>

</body>
</html>
```